Emergency Response Company Needs a Web Design

To go along with a completed logo redesign, we are looking to update and modernize the design and feel of our site.The emergency response planning we do is based around the oil and gas industry. Our existing site at http://www.quorvanteplan.com/ will give some insight in to what we do. For more related insight, here are some direct competitors:
http://www.lumeridgecare.ca/index.php
http://www.tessorwindplan.com/
http://pollixfuels.com/
http://dravonltd.ca/company.php
http://www.keel-aidworks.com/

Industry/Entity Type

Oil And Gas

```html
<!DOCTYPE html>
<html lang="en">
<head>
<meta charset="utf-8">
<title>Quorvante Resource Consultants</title>
<link rel="stylesheet" href="https://fonts.googleapis.com/css2?family=Nunito+Sans:wght@300;400;600;700&family=Open+Sans:wght@400;600&display=swap">
<style>
  :root {
    --canvas: #f0f0f0;
    --page: #ffffff;
    --red: #c8102e;
    --red-bright: #e31b23;
    --red-dark: #a30d22;
    --ink: #333333;
    --ink-soft: #555555;
    --muted: #8a8a8a;
    --footer: #000000;
  }
  * { box-sizing: border-box; margin: 0; padding: 0; }
  html, body { width: 1200px; height: 1075px; overflow: hidden; }
  body { background: var(--canvas); font-family: "Open Sans", sans-serif; color: var(--ink); }
  .page { position: absolute; left: 179px; top: 0; width: 840px; height: 1075px; background: var(--page); }

  .site-header { position: absolute; left: 0; top: 0; width: 840px; height: 107px; }
  .brand { position: absolute; left: 32px; top: 30px; display: flex; align-items: center; gap: 10px; }
  .brand-mark { width: 14px; height: 14px; background: var(--red); }
  .brand-name { font-family: "Nunito Sans", sans-serif; font-weight: 400; color: #2a2a2a; line-height: 1; }
  .brand-name .main { display: block; font-size: 32px; letter-spacing: 0.5px; }
  .brand-name .sub { display: block; font-size: 11.5px; margin-top: 5px; letter-spacing: 0.2px; }
  .support { position: absolute; right: 24px; top: 48px; text-align: right; font-family: "Nunito Sans", sans-serif; }
  .support .label { font-size: 14px; color: var(--muted); font-weight: 300; }
  .support .phone { font-size: 21px; color: var(--ink-soft); margin-top: 1px; }

  .main-nav { position: absolute; left: 0; top: 107px; width: 840px; height: 42px; display: flex;
    background: linear-gradient(#d01a33, var(--red-dark)); }
  .main-nav a { display: flex; align-items: center; justify-content: center; height: 42px; color: #fff;
    text-decoration: none; font-family: "Nunito Sans", sans-serif; font-size: 14px; border-right: 1px solid rgba(255,255,255,0.25); }
  .main-nav a:last-child { border-right: 0; justify-content: flex-start; padding-left: 27px; }

  .hero { position: absolute; left: 0; top: 149px; width: 840px; height: 374px; overflow: hidden;
    background: linear-gradient(100deg, #5a4a3a 0%, #8a7a68 25%, #b8c4d0 45%, #c9d6e2 60%, #d9a97a 78%, #b4c84a 100%); }
  .hero-caption { position: absolute; left: 0; top: 126px; width: 373px; height: 144px; background: rgba(15,15,15,0.85);
    padding: 22px 0 0 35px; }
  .hero-caption h1 { font-family: "Nunito Sans", sans-serif; font-weight: 400; font-size: 28px; line-height: 33px; color: #fff; }
  .hero-caption h1 span { display: block; color: var(--red-bright); }
  .hero-caption p { font-size: 10.5px; line-height: 16px; color: #ddd; margin-top: 8px; }
  .hero-dots { position: absolute; left: 393px; top: 351px; display: flex; gap: 4px; }
  .hero-dots span { width: 11px; height: 11px; border-radius: 50%; background: #fff; }

  .services { position: absolute; top: 543px; left: 0; width: 840px; }
  .service { position: absolute; width: 250px; }
  .service-photo { width: 250px; height: 94px; }
  .service h2 { font-family: "Nunito Sans", sans-serif; font-weight: 400; font-size: 17px; color: var(--red); margin-top: 12px; }
  .service p { font-size: 10.5px; line-height: 16.5px; color: var(--muted); margin-top: 5px; }
  .btn { display: inline-block; margin-top: 11px; width: 88px; height: 26px; line-height: 26px; text-align: center;
    background: linear-gradient(var(--red-bright), #c40f17); color: #fff; font-size: 10.5px; font-weight: 600;
    text-decoration: none; border-radius: 2px; }

  .about { position: absolute; left: 32px; top: 793px; width: 510px; }
  .about h2, .contact h2 { font-family: "Nunito Sans", sans-serif; font-weight: 300; font-size: 25px; color: #333; }
  .about p { font-size: 10.5px; line-height: 18px; color: var(--ink-soft); margin-top: 10px; }
  .about p.secondary { color: var(--muted); margin-top: 9px; }
  .contact { position: absolute; left: 578px; top: 794px; width: 240px; }
  .contact ul { list-style: none; margin-top: 10px; }
  .contact li { font-size: 10.5px; line-height: 22px; color: #333; }

  .site-footer { position: absolute; left: 0; top: 985px; width: 840px; height: 90px; background: var(--footer); padding: 21px 0 0 35px; }
  .footer-nav { font-family: "Nunito Sans", sans-serif; font-size: 12px; color: #fff; }
  .footer-nav a { color: #fff; text-decoration: none; }
  .footer-nav .sep { margin: 0 5px; }
  .copyright { font-family: "Nunito Sans", sans-serif; font-size: 9.5px; color: #bbb; margin-top: 10px; }
</style>
</head>
<body>
<div class="page">
  <header class="site-header">
    <div class="brand">
      <div class="brand-name"><span class="main">QUORVANTE</span><span class="sub">RESOURCE CONSULTANTS LTD</span></div>
      <span class="brand-mark"></span>
    </div>
    <div class="support">
      <div class="label">Consulation &amp; Support</div>
      <div class="phone">555.318.4420</div>
    </div>
  </header>

  <nav class="main-nav">
    <a href="#" style="width:113px">HOME</a>
    <a href="#" style="width:125px">ABOUT US</a>
    <a href="#" style="width:139px">SOLUTIONS</a>
    <a href="#" style="width:120px">TRAINING</a>
    <a href="#" style="width:116px">CAREERS</a>
    <a href="#" style="width:227px">CONTACT US</a>
  </nav>

  <section class="hero" role="img" aria-label="Photo of a smiling engineer in a yellow hard hat and safety vest at a refinery">
    <div class="hero-caption">
      <h1>Petroleum Engineering <span>Consultants</span></h1>
      <p>Cum sociis natoque penatibus et magnis dis parturient montes nascetur ridiculus mus In iaculis facilisis massa Etiam</p>
    </div>
    <div class="hero-dots"><span></span><span></span><span></span><span></span></div>
  </section>

  <section class="services">
    <article class="service" style="left:27px">
      <div class="service-photo" role="img" aria-label="Photo of a lit industrial plant at dusk" style="background:linear-gradient(90deg,#c98a2a,#2b3f9a 45%,#1e2f7a)"></div>
      <h2>Public Resources</h2>
      <p>Proin nulla arcu nonummy luctus dictum eget fermentum et lorem Nunc porta convallis</p>
      <a class="btn" href="#">READ MORE</a>
    </article>
    <article class="service" style="left:295px">
      <div class="service-photo" role="img" aria-label="Photo of two workers in hard hats reviewing plans" style="background:linear-gradient(90deg,#8d8a85,#d8c34a 40%,#b7c25a 70%,#7a6f66)"></div>
      <h2>Staff Resources</h2>
      <p>Proin nulla arcu nonummy luctus dictum eget fermentum et lorem Nunc porta convallis</p>
      <a class="btn" href="#">READ MORE</a>
    </article>
    <article class="service" style="left:564px">
      <div class="service-photo" role="img" aria-label="Photo of a worker in red coveralls operating a wellhead valve" style="background:linear-gradient(90deg,#7fb0d6,#c9333a 35%,#8ab8da 70%,#6a9cc4)"></div>
      <h2>Certified ICS Training</h2>
      <p>Proin nulla arcu nonummy luctus dictum eget fermentum et lorem Nunc porta convallis</p>
      <a class="btn" href="#">READ MORE</a>
    </article>
  </section>

  <section class="about">
    <h2>About Quorvante Resources Consultants</h2>
    <p>Phasellus felis dolor scelerisque a tempus eget lobortis id libero Donec scelerisque leo ac risus Praesent sit amet est In dictum dolor eu dictum porttitor enim felis viverra mi eget luctus</p>
    <p class="secondary">Praesent elementum elit at tellus nec ultricies sit amet porttitor mattis enim In massa libero interdum nec interdum vel blandit sed nulla In ullamcorper est eget tempor cursus neque mi consectetuer mi ultricies massa est sed nisl Class aptent taciti sociosqu ad litora torquent per conubia nostra</p>
  </section>

  <section class="contact">
    <h2>Contact Us</h2>
    <ul>
      <li>410, 722 - 9 Avenue SW Calgary, AB T2P 1K4</li>
      <li>Tel: 403-555-0142 (24 Hrs)</li>
      <li>Fax: 403-555-0187 (24 Hrs)</li>
      <li>Email: mail@quorvanteplan.com</li>
    </ul>
  </section>

  <footer class="site-footer">
    <nav class="footer-nav">
      <a href="#">HOME</a><span class="sep">|</span><a href="#">ABOUT US</a><span class="sep">|</span><a href="#">SOLUTIONS</a><span class="sep">|</span><a href="#">TRAINING</a><span class="sep">|</span><a href="#">CAREERS</a><span class="sep">|</span><a href="#">CONTACT US</a>
    </nav>
    <p class="copyright">© 2014 Company Name &nbsp;All right reserved &nbsp;Term of Use</p>
  </footer>
</div>
</body>
</html>
```